Business Card Design Project

Hello
I want a Simple Business card that uses the company logo that is easily reasonable but looks professional as I am an IT Services company and would look to share these cards with prospective clients.
The details are:
Kestrel Arc Solutions
14 Morrow Lane
Birmingham
B7 4QX
Telephone 0845 217 6640
I would like my name Oliver Hastings and my title Director on the card.
Target Market(s)
IT Professionals
Industry/Entity Type
Business

```html
<!DOCTYPE html>
<html lang="en">
<head>
<meta charset="utf-8">
<title>Kestrel Arc Solutions – Business Cards</title>
<link rel="stylesheet" href="https://fonts.googleapis.com/css2?family=Jost:ital,wght@0,400;0,500;0,700;1,400;1,500&display=swap">
<style>
  :root {
    --backdrop: #e9e9e6;
    --card: #ffffff;
    --ink: #2b2b2b;
    --lime: #8fdc3a;
    --lime-soft: #c8ee8a;
    --yellow-soft: #eef3a0;
    --aqua-soft: #cfe9dc;
    --shadow: rgba(0,0,0,0.12);
  }
  * { box-sizing: border-box; margin: 0; padding: 0; }
  html, body { width: 851px; height: 1200px; overflow: hidden; }
  body {
    background: var(--backdrop);
    font-family: "Jost", "Futura", sans-serif;
    color: var(--ink);
  }
  .sheet {
    width: 851px; height: 1200px;
    display: flex; flex-direction: column; justify-content: space-around;
    padding: 60px 0;
  }
  .concept { display: flex; justify-content: center; gap: 40px; }
  .card {
    position: relative;
    width: 360px; height: 220px;
    background: var(--card);
    box-shadow: 0 6px 18px var(--shadow);
    overflow: hidden;
  }
  address { font-style: normal; }

  /* Logo side */
  .card--logo { display: flex; align-items: center; justify-content: center; gap: 12px; }
  .brand-name { font-size: 27px; font-weight: 700; letter-spacing: -0.5px; color: var(--ink); }
  .brand-dot { width: 22px; height: 22px; border-radius: 50%; background: var(--lime); }

  /* Concept one: lime name panel */
  .name-panel {
    position: absolute; left: 192px; top: 18px; width: 150px; height: 92px;
    border-radius: 46px;
    background: linear-gradient(135deg, var(--lime), var(--lime-soft));
  }
  .name-panel-text {
    position: absolute; left: 212px; top: 40px; width: 120px; color: #fff;
  }
  .name-panel-text .name { font-size: 16px; font-weight: 500; font-style: italic; line-height: 1.2; }
  .name-panel-text .role { font-size: 12px; font-style: italic; }
  .tel { font-size: 16px; font-weight: 700; }
  .card--panel .tel { position: absolute; left: 22px; top: 24px; }
  .address { font-size: 11.5px; line-height: 1.35; font-weight: 500; }
  .card--panel .address { position: absolute; left: 22px; bottom: 20px; }

  /* Concept two: soft foliage */
  .foliage {
    position: absolute; right: 20px; bottom: 14px; width: 170px; height: 130px;
    border-radius: 50% 50% 45% 45%;
    background: radial-gradient(ellipse at 45% 45%, var(--aqua-soft), var(--lime-soft) 45%, var(--yellow-soft) 70%, transparent 72%);
    opacity: 0.6;
  }
  .card--foliage .details { position: absolute; left: 22px; top: 22px; }
  .card--foliage .name { font-size: 16px; font-weight: 700; }
  .card--foliage .role { font-size: 13px; font-style: italic; margin-bottom: 8px; }
  .card--foliage .tel { position: absolute; left: 22px; bottom: 22px; }
</style>
</head>
<body>
<main class="sheet">

  <section class="concept concept--panel">
    <article class="card card--panel">
      <div class="name-panel" role="img" aria-label="Lime decorative shape behind the name"></div>
      <div class="name-panel-text">
        <p class="name">Oliver Hastings</p>
        <p class="role">Director</p>
      </div>
      <p class="tel">Tel: 0845 217 6640</p>
      <address class="address">
        Kestrel Arc Solutions<br>14 Morrow Lane<br>Birmingham<br>B7 4QX
      </address>
    </article>
    <article class="card card--logo">
      <span class="brand-name">Kestrel Arc Solutions</span>
      <span class="brand-dot" aria-hidden="true"></span>
    </article>
  </section>

  <section class="concept concept--foliage">
    <article class="card card--foliage">
      <div class="foliage" role="img" aria-label="Faint pastel tree illustration"></div>
      <div class="details">
        <p class="name">Oliver Hastings</p>
        <p class="role">Director</p>
        <address class="address">
          Kestrel Arc Solutions<br>14 Morrow Lane<br>Birmingham<br>B7 4QX
        </address>
      </div>
      <p class="tel">Tel: 0845 217 6640</p>
    </article>
    <article class="card card--logo">
      <span class="brand-name">Kestrel Arc Solutions</span>
      <span class="brand-dot" aria-hidden="true"></span>
    </article>
  </section>

</main>
</body>
</html>
```